Green Energy Conservation Business Cards

We believe in Conserve before you produce energy. I am looking for a unique, bold business card. that Demonstrates Expertise in our field. I would be interested to try and incorporate a night picture of the US or world showing the yellow lights on one side. I would be open to a design that caters to half the business card size height and same length. Our primary expertise is Energy projects for self storage. Use either black or white background .Attached are the logos and symbols.

May I see some design utilizing a smaller business card. the same length as a normal business card but cut in half on the height. best regards Garrick

```html
<!DOCTYPE html>
<html lang="en">
<head>
<meta charset="utf-8">
<title>Verdant Energy Group – Business Card</title>
<link rel="stylesheet" href="https://fonts.googleapis.com/css2?family=Montserrat:wght@400;500;600;700&display=swap">
<style>
  :root {
    --backdrop: #e9e9ea;
    --card: #ffffff;
    --brand-blue: #1261ad;
    --brand-green: #6cbe2e;
    --light-green: #a6d63c;
    --ink-grey: #4d4d4f;
    --text-white: #ffffff;
  }
  html, body {
    margin: 0;
    padding: 0;
    width: 1200px;
    height: 718px;
    overflow: hidden;
    background: var(--backdrop);
    font-family: "Montserrat", Arial, sans-serif;
  }
  .stage {
    position: relative;
    width: 1200px;
    height: 718px;
  }
  .business-card {
    position: absolute;
    left: 150px;
    top: 102px;
    width: 900px;
    height: 514px;
    background: var(--card);
    box-shadow: 0 10px 30px rgba(0,0,0,0.12);
    overflow: hidden;
  }
  .swoosh {
    position: absolute;
    inset: 0;
    width: 900px;
    height: 514px;
  }
  .brand-name {
    position: absolute;
    left: 70px;
    top: 222px;
    margin: 0;
    font-size: 30px;
    font-weight: 600;
    letter-spacing: 1px;
    color: var(--brand-blue);
    line-height: 1;
    white-space: nowrap;
  }
  .person {
    position: absolute;
    right: 60px;
    top: 58px;
    text-align: right;
  }
  .person-name {
    margin: 0;
    font-size: 27px;
    font-weight: 600;
    letter-spacing: 1px;
    color: var(--brand-blue);
  }
  .person-role {
    margin: 4px 0 0;
    font-size: 13px;
    font-weight: 500;
    letter-spacing: 2px;
    color: var(--ink-grey);
  }
  .contacts {
    position: absolute;
    right: 60px;
    top: 132px;
    margin: 0;
    padding: 0;
    list-style: none;
  }
  .contacts li {
    display: flex;
    justify-content: flex-end;
    align-items: center;
    gap: 10px;
    font-size: 14px;
    color: var(--ink-grey);
    height: 26px;
  }
  .contacts svg {
    width: 14px;
    height: 14px;
    flex: none;
  }
  .address {
    position: absolute;
    left: 64px;
    bottom: 32px;
    margin: 0;
    font-style: normal;
    font-size: 19px;
    font-weight: 500;
    line-height: 1.35;
    color: var(--text-white);
    letter-spacing: 0.5px;
  }
</style>
</head>
<body>
<main class="stage">
  <article class="business-card">
    <svg class="swoosh" viewBox="0 0 900 514" aria-hidden="true">
      <path d="M0,408 C320,392 620,362 900,292 L900,310 C620,382 320,404 0,414 Z" fill="var(--light-green)"/>
      <path d="M0,414 C320,404 620,384 900,310 L900,322 C620,396 320,412 0,418 Z" fill="var(--brand-green)"/>
      <path d="M0,428 C320,420 620,406 900,336 L900,514 L0,514 Z" fill="var(--brand-blue)"/>
    </svg>

    <p class="brand-name">Verdant Energy Group</p>

    <header class="person">
      <h1 class="person-name">DUSTIN GARRICK</h1>
      <p class="person-role">FINANCIAL ADVISOR</p>
    </header>

    <ul class="contacts">
      <li>014 552 7310
        <svg viewBox="0 0 14 14"><path d="M3 1h3l1 3-2 1a7 7 0 0 0 4 4l1-2 3 1v3a1 1 0 0 1-1 1A11 11 0 0 1 2 2a1 1 0 0 1 1-1z" fill="none" stroke="var(--ink-grey)" stroke-width="1.2"/></svg>
      </li>
      <li>014 552 7311
        <svg viewBox="0 0 14 14"><rect x="4" y="1" width="6" height="12" rx="1" fill="var(--brand-green)"/></svg>
      </li>
      <li>014 552 7312
        <svg viewBox="0 0 14 14"><rect x="1" y="3" width="12" height="9" rx="1" fill="var(--brand-green)"/></svg>
      </li>
      <li>info@verdantenergy.com
        <svg viewBox="0 0 14 14"><rect x="1" y="3" width="12" height="8" fill="var(--brand-green)"/><path d="M1 3l6 5 6-5" fill="none" stroke="#fff" stroke-width="1"/></svg>
      </li>
      <li>www.verdantenergy.com
        <svg viewBox="0 0 14 14"><circle cx="7" cy="7" r="6" fill="var(--brand-green)"/></svg>
      </li>
    </ul>

    <address class="address">214 (3rd floor) Mill,<br>Harbour Road QTS</address>
  </article>
</main>
</body>
</html>
```